After-School Program - End of the Year Mailing to Donors

We would like to highlight some of our accomplishments from the year and ask people to donate to our organization. We are a non-profit organization that serves underprivileged children with after school programs. We want a 6x9 flyer with printing on both sides that we can mail out soon. The flyer should be a mix of great photos, some text, and a space for mailing and return address.

Target Market(s)

regular donors

Industry/Entity Type

Education

Font styles to use
Serif

Colors

Designer to choose colors to be used in the design.

Requirements
Must have
• Photos, text, a space on one side for a mailing label, a return address, and a stamp.
Nice to have
• attractive, eye-catching
Should not have
• boring

```html
<!DOCTYPE html>
<html lang="en">
<head>
<meta charset="utf-8">
<title>Brightway Family Learning Center – Donor Postcard</title>
<link rel="stylesheet" href="https://fonts.googleapis.com/css2?family=Oswald:wght@500;600;700&family=Open+Sans:ital,wght@0,400;0,600;0,700;1,600;1,700&display=swap">
<style>
  :root {
    --bg: #bdbdbd;
    --card: #ffffff;
    --panel: #dfe5ec;
    --panel-light: #e9edf2;
    --blue: #1e88e0;
    --blue-band: #2f82c4;
    --red: #c0162b;
    --ink: #1b1b1b;
    --gold-a: #c9a661;
    --gold-b: #f0dcae;
    --photo-a: #5a5f8f;
    --photo-b: #c23a3a;
    --park-a: #6e9a4e;
    --park-b: #9cb6d6;
  }
  * { box-sizing: border-box; margin: 0; padding: 0; }
  html, body { width: 1154px; height: 1200px; overflow: hidden; }
  body { background: var(--bg); font-family: "Open Sans", sans-serif; color: var(--ink); position: relative; }

  .postcard {
    position: absolute; left: 172px; width: 810px; height: 540px;
    background: var(--card); overflow: hidden;
    box-shadow: 0 6px 18px rgba(0,0,0,.25);
  }
  .postcard--front { top: 45px; background: #c9ccd1; }
  .postcard--back { top: 625px; }

  /* FRONT */
  .hero-photo {
    position: absolute; left: 0; top: 0; width: 560px; height: 330px;
    border-radius: 0 0 26px 0;
    background: linear-gradient(160deg, var(--photo-a) 0%, #6d6f9c 45%, var(--photo-b) 85%, #e06a9a 100%);
  }
  .headline-panel {
    position: absolute; left: 0; top: 345px; width: 560px; height: 195px;
    background: var(--panel-light); border-radius: 0 26px 0 0;
    padding: 42px 0 0 36px;
  }
  .headline {
    font-family: "Oswald", sans-serif; font-weight: 700; line-height: 1;
    text-transform: uppercase; letter-spacing: .5px;
  }
  .headline__line1 { color: var(--blue); font-size: 64px; display: block; }
  .headline__line2 { color: var(--red); font-size: 70px; display: block; margin-top: 2px; }

  .brand-box {
    position: absolute; left: 575px; top: 0; width: 235px; height: 165px;
    background: #f4f4f5; border-radius: 0 0 0 26px;
    display: flex; flex-direction: column; align-items: center; justify-content: center; gap: 10px;
    text-align: center; padding: 0 18px;
  }
  .brand-mark { width: 46px; height: 46px; border-radius: 50%; background: #f2dc1e; }
  .brand-name { font-weight: 700; font-size: 15px; line-height: 1.25; color: var(--ink); }

  .about-box {
    position: absolute; left: 575px; top: 180px; width: 235px; height: 360px;
    background: linear-gradient(135deg, var(--gold-a), var(--gold-b));
    border-radius: 26px 0 0 0;
    padding: 46px 20px 0 22px;
  }
  .about-box__title {
    font-family: "Oswald", sans-serif; font-weight: 600; font-size: 24px;
    color: var(--red); text-transform: uppercase; margin-bottom: 6px;
  }
  .about-box__text { font-size: 12.6px; font-weight: 600; line-height: 1.42; text-align: justify; }
  .link { color: var(--blue); font-weight: 700; font-style: italic; }

  /* BACK */
  .message-side {
    position: absolute; left: 0; top: 0; width: 555px; height: 540px; background: var(--panel);
  }
  .gold-tab { position: absolute; background: linear-gradient(135deg, var(--gold-a), var(--gold-b)); }
  .gold-tab--left { left: 0; top: 0; width: 62px; height: 170px; border-radius: 0 0 22px 0; }
  .gold-tab--right { left: 330px; top: 0; width: 225px; height: 62px; border-radius: 0 0 0 22px; }
  .event-photo {
    position: absolute; left: 76px; top: 0; width: 240px; height: 150px;
    border-radius: 0 0 24px 24px;
    background: linear-gradient(180deg, var(--park-b) 0%, var(--park-a) 55%, #b84b4b 80%, var(--park-a) 100%);
  }
  .back-brand {
    position: absolute; left: 370px; top: 80px; width: 160px;
    display: flex; flex-direction: column; align-items: center; gap: 8px; text-align: center;
  }
  .back-brand .brand-name { font-size: 13px; }
  .back-brand .brand-mark { width: 38px; height: 38px; }

  .appeal {
    position: absolute; left: 26px; top: 200px; width: 505px;
    font-size: 12.6px; line-height: 1.45; text-align: justify;
  }
  .appeal .amount { color: var(--red); font-weight: 700; font-style: italic; }
  .appeal .link { color: var(--red); }

  .contact-band {
    position: absolute; left: 26px; top: 372px; height: 32px; width: 270px;
    background: var(--blue-band); color: #fff;
    font-family: "Oswald", sans-serif; font-weight: 600; font-size: 21px;
    letter-spacing: 1px; text-transform: uppercase; padding: 1px 0 0 12px;
    clip-path: polygon(0 0, 100% 0, 94% 100%, 0 100%);
  }
  .contact {
    position: absolute; left: 30px; top: 414px; font-size: 14px; font-weight: 600; line-height: 1.32;
  }
  .contact__org { color: var(--blue-band); font-style: italic; font-weight: 700; }
  .social-note {
    position: absolute; left: 30px; top: 502px;
    font-family: "Oswald", sans-serif; font-weight: 500; font-size: 18px; color: var(--red);
  }

  .address-side { position: absolute; left: 555px; top: 0; width: 255px; height: 540px; }
  .return-address { position: absolute; left: 16px; top: 52px; font-size: 9.5px; font-weight: 700; line-height: 1.3; }
  .stamp-box { position: absolute; right: 30px; top: 18px; width: 66px; height: 66px; border: 1.5px solid var(--ink); }
  .address-lines { position: absolute; left: 40px; top: 260px; width: 190px; height: 120px; }
</style>
</head>
<body>

<section class="postcard postcard--front" aria-label="Postcard front">
  <div class="hero-photo" role="img" aria-label="Photo of two smiling children wearing reindeer antler headbands"></div>

  <div class="headline-panel">
    <h1 class="headline">
      <span class="headline__line1">Give a</span>
      <span class="headline__line2">Hand to us !</span>
    </h1>
  </div>

  <div class="brand-box">
    <span class="brand-mark" aria-hidden="true"></span>
    <span class="brand-name">Brightway Family Learning Center</span>
  </div>

  <div class="about-box">
    <h2 class="about-box__title">What we do</h2>
    <p class="about-box__text">We serve over 150 children each day at our four sites with a unique mix of homework help, a focus on literacy, enrichment classes - including music lessons, and a caring environment based on God's love. Please help us continue to impact children and families through our high quality faith-based educational programs. To contribute, please visit <span class="link">www.brightwaykids.org</span> and click on the donate button.</p>
  </div>
</section>

<section class="postcard postcard--back" aria-label="Postcard back">
  <div class="message-side">
    <div class="gold-tab gold-tab--left"></div>
    <div class="event-photo" role="img" aria-label="Group photo of program children gathered on a grassy park lawn"></div>
    <div class="gold-tab gold-tab--right"></div>

    <div class="back-brand">
      <span class="brand-mark" aria-hidden="true"></span>
      <span class="brand-name">Brightway Family Learning Center</span>
    </div>

    <p class="appeal">Brightway Family Learning Center is in the middle of its 24th year of ministry and we need your help to finish our year strong! We need another <span class="amount">$35,000</span> from our individual donors to help us meet our budget. We serve over 150 children each day at our four sites with a unique mix of homework help, a focus on literacy, enrichment classes - including music lessons, and a caring environment based on God's love. Please help us continue to impact children and families through our high quality faith-based educational programs. To contribute, please visit <span class="link">www.brightwaykids.org</span> and click on the donate button.</p>

    <div class="contact-band">Contact us</div>
    <address class="contact" style="font-style:normal">
      <div class="contact__org">Brightway Family Learning Center</div>
      <div>214 Alder Grove Ave.</div>
      <div>Riverton, CA 90412</div>
      <div>(555) 014-2290</div>
      <div>www.brightwaykids.org</div>
    </address>
    <p class="social-note">Find us on our social page - search Brightway Family Learning Center</p>
  </div>

  <div class="address-side">
    <address class="return-address" style="font-style:normal">214 Alder Grove Ave.<br>Riverton, CA 90412</address>
    <div class="stamp-box" aria-label="Stamp area"></div>
    <svg class="address-lines" viewBox="0 0 190 120" aria-label="Mailing address lines">
      <line x1="0" y1="10" x2="190" y2="10" stroke="#1b1b1b" stroke-width="1.5"/>
      <line x1="0" y1="55" x2="190" y2="55" stroke="#1b1b1b" stroke-width="1.5"/>
      <line x1="0" y1="100" x2="190" y2="100" stroke="#1b1b1b" stroke-width="1.5"/>
    </svg>
  </div>
</section>

</body>
</html>
```